Harbor Crest Vitality.com Landing Page

Create a well designed home/landing page using that communicates the feeling of Harbor Crest Vitality with this sections that scroll from top to bottom -
Top section - Displays "Harbor Crest Vitality" with space for embedded YouTube video.

The following sections follow the top section -
Assess your current Harbor Crest Vitality. Complete our free life balance assessment to identify key areas where you you will most benefit.
"Learn more" call to action button

Create a Harbor Crest Vitality Learning Portal account. Get a 14 day free trial to a wealth of learning activities, motivational videos and professional presentations on our learning portal designed specifically to address the eight essential areas of Harbor Crest Vitality.
"Register now" call to action button

Get weekly reports on your progress and goal achievement. Celebrate your success each week as you review your progress on each life balance area.

Appropriate royalty free photos and graphics that fit the chosen theme you recommend.

I'm reviewing the designs. I realize that I need to clarify that Harbor Crest Vitality focuses on eight areas, not just physical fitness and meditation. Spirituality and Sense of Purpose; Fitness and Health; Relationships; Personal Finance; Recreation and Fun; Physical Environment; Personal Development and Learning; Work and Career

1 page

33a6d7
00a990
9bcb3c
2f73b3

```html
<!DOCTYPE html>
<html lang="en">
<head>
<meta charset="utf-8">
<title>Harbor Crest Vitality</title>
<link rel="stylesheet" href="https://fonts.googleapis.com/css2?family=IBM+Plex+Serif:wght@400;600;700&display=swap">
<style>
  :root {
    --sky-blue: #33a6d7;
    --teal: #00a990;
    --lime: #9bcb3c;
    --ocean: #2f73b3;
    --white: #ffffff;
    --ink: #333333;
    --serif: "IBM Plex Serif", Georgia, serif;
  }
  * { box-sizing: border-box; margin: 0; padding: 0; }
  html, body { width: 1200px; height: 2440px; overflow: hidden; background: var(--white); }
  body { font-family: var(--serif); color: var(--white); }
  .page { position: relative; width: 1200px; height: 2440px; }

  .hero {
    position: absolute; left: 0; top: 0; width: 1200px; height: 635px;
    background:
      linear-gradient(180deg, rgba(10,50,60,0) 45%, rgba(10,60,60,0.55) 100%),
      linear-gradient(115deg, #1a8fc4 0%, #0aa0a0 40%, #1aa27a 65%, #6cb83e 100%);
  }
  .hero-title {
    position: absolute; left: 0; right: 0; top: 58px;
    text-align: center; font-size: 62px; font-weight: 700; letter-spacing: -0.5px;
    color: var(--white);
  }
  .video-play { position: absolute; left: 295px; top: 277px; }

  .feature { position: absolute; left: 0; width: 1200px; height: 570px; overflow: hidden; }
  .feature-photo { position: absolute; inset: 0; }
  .panel { position: absolute; bottom: 0; height: 457px; }
  .panel-right { left: 507px; right: 0; border-radius: 228px 0 0 228px; }
  .panel-left { left: 0; width: 712px; border-radius: 0 228px 228px 0; }

  .assess { top: 635px; }
  .assess .feature-photo { background: linear-gradient(180deg, #e4f6f4 0%, #8fc7b8 35%, #4f8f72 55%, #8aa39a 75%, #b8aa95 100%); }
  .assess .panel { background: var(--teal); }

  .portal { top: 1205px; }
  .portal .feature-photo { background: linear-gradient(160deg, #b8d5e6 0%, #f4e3c8 35%, #f7c99a 55%, #f2d6c8 75%, #c7dceb 100%); }
  .portal .panel { background: var(--ocean); }

  .reports { top: 1774px; }
  .reports .feature-photo { background: linear-gradient(180deg, #d7e3ea 0%, #eef0ea 40%, #b9c6c4 70%, #6f7d5e 100%); }
  .reports .panel { background: var(--lime); }

  .copy { position: absolute; }
  .heading { font-weight: 600; font-size: 36px; line-height: 41px; }
  .body { font-weight: 400; font-size: 22px; line-height: 27px; margin-top: 18px; }
  .cta {
    display: flex; align-items: center; justify-content: center;
    width: 174px; height: 49px; border: 3px solid var(--white);
    font-family: var(--serif); font-size: 15px; font-weight: 700; letter-spacing: 0.3px;
    color: var(--white); text-transform: uppercase; text-decoration: none;
  }

  .assess .copy { left: 140px; top: 88px; }
  .assess .cta { margin: 22px 0 0 14px; }

  .portal .copy { left: 185px; top: 95px; width: 480px; }
  .portal .heading { font-size: 28px; line-height: 33px; }
  .portal .offer { font-size: 42px; font-weight: 600; line-height: 50px; margin-top: 6px; }
  .portal .body { font-size: 16px; line-height: 21px; margin-top: 8px; }
  .portal .cta { margin-top: 20px; }

  .reports .copy { left: 140px; top: 80px; }
  .reports .body { font-size: 19.5px; line-height: 23px; margin-top: 12px; }
  .reports .cta { margin-top: 22px; }

  .footer {
    position: absolute; left: 0; top: 2343px; width: 1200px; height: 97px;
    display: flex; align-items: center; justify-content: center;
    font-size: 16px; color: var(--ink);
  }
</style>
</head>
<body>
<div class="page">

  <header class="hero" role="img" aria-label="Woman in a yoga pose on a deck facing misty mountains, tinted blue to green">
    <h1 class="hero-title">Harbor Crest Vitality</h1>
    <svg class="video-play" width="142" height="142" viewBox="0 0 142 142" aria-label="Play video">
      <circle cx="71" cy="71" r="71" fill="#ffffff" fill-opacity="0.22"/>
      <circle cx="71" cy="71" r="42" fill="#ffffff" fill-opacity="0.45"/>
      <path d="M62 52 L86 71 L62 90 Z" fill="#ffffff"/>
    </svg>
  </header>

  <section class="feature assess">
    <div class="feature-photo" role="img" aria-label="Woman meditating cross-legged on a lakeside dock with forested hills"></div>
    <div class="panel panel-right">
      <div class="copy">
        <h2 class="heading">Assess your current<br>Harbor Crest Vitality.</h2>
        <p class="body">Complete our free life balance<br>assessment to identify key areas<br>where you you will most benefit.</p>
        <a class="cta" href="#">Learn more</a>
      </div>
    </div>
  </section>

  <section class="feature portal">
    <div class="feature-photo" role="img" aria-label="Woman in a white dress raising her arms toward a pastel sunset sky"></div>
    <div class="panel panel-left">
      <div class="copy">
        <h2 class="heading">Create a Harbor Crest Vitality<br>Learning Portal account.</h2>
        <p class="offer">Get a 14 day free trial</p>
        <p class="body">to a wealth of learning activities, motivational videos and professional presentations on our learning portal designed specifically to address the eight essential areas of Harbor Crest Vitality.</p>
        <a class="cta" href="#">Register now</a>
      </div>
    </div>
  </section>

  <section class="feature reports">
    <div class="feature-photo" role="img" aria-label="Woman in tree pose on a grassy seaside cliff at sunrise"></div>
    <div class="panel panel-right">
      <div class="copy">
        <h2 class="heading">Get weekly reports on<br>your progress and goal<br>achievement.</h2>
        <p class="body">Celebrate your success each week as<br>you review your progress on each life<br>balance area.</p>
        <a class="cta" href="#">Learn more</a>
      </div>
    </div>
  </section>

  <footer class="footer">Copyright 2020 Harbor Crest Vitality.com All Rights Reserved</footer>

</div>
</body>
</html>
```